KT Crewing business card

Require business card which includes:
Company name: KT CREWING PTY LTD
Email: Mick@ktcrewing.com.au
Phone: 0431 256 049
ACN: 718 235 946

slogan: Onsite Auto Electrician Labour hire

Details and logo on top side
Logo only on bottom side

colour codes : #F15A29 , #939598

Target Market(s)

Western Australia mining sector

Industry/Entity Type

Mining

Contact Information for Business Card

Require business card which includes: Company name: KT CREWING PTY LTD Email: Mick@ktcrewing.com.au Phone: 0431 256 049 ACN: 718 235 946 slogan: Onsite Auto Electrician Labour hire Details and logo on top side Logo only on bottom side colour codes : #F15A29 , #939598

Colors
EE7325
F08F49
F5BC92
FAE3D3
FDF4ED

Requirements
Must have
• double sided

```html
<!DOCTYPE html>
<html lang="en">
<head>
<meta charset="utf-8">
<title>KT Crewing business card</title>
<link rel="stylesheet" href="https://fonts.googleapis.com/css2?family=Exo+2:wght@300;400;600;700;800&display=swap">
<style>
  :root {
    --orange: #F15A29;
    --grey: #939598;
    --text-grey: #808285;
    --white: #ffffff;
    --card-black: #1b1b1c;
    --stage: #2b2b2d;
  }
  * { margin: 0; padding: 0; box-sizing: border-box; }
  html, body {
    width: 1200px; height: 1108px; overflow: hidden;
    background: var(--stage);
    font-family: "Exo 2", "Segoe UI", sans-serif;
  }
  .stage {
    position: relative; width: 1200px; height: 1108px;
  }
  .card {
    position: absolute; top: 229px;
    width: 400px; height: 650px;
    border-radius: 22px; overflow: hidden;
  }
  .card--front { left: 150px; background: var(--white); }
  .card--back { left: 650px; background: var(--card-black); }

  .brand-mark {
    position: absolute; left: 0; right: 0; top: 150px;
    text-align: center;
    font-weight: 800; font-size: 66px; line-height: 1;
    color: var(--orange); letter-spacing: 1px;
  }
  .contact {
    position: absolute; left: 0; right: 0; top: 330px;
    text-align: center; color: var(--text-grey);
  }
  .contact__name {
    font-weight: 700; font-size: 25px; color: var(--orange);
    letter-spacing: 0.5px;
  }
  .contact__role {
    font-weight: 300; font-size: 18px; margin-top: 2px;
  }
  .contact__rule {
    width: 112px; height: 1.5px; background: var(--orange);
    margin: 16px auto;
  }
  .contact__line { font-weight: 300; font-size: 18px; line-height: 1.35; }
  .contact__label { color: var(--orange); }

  .slogan-band {
    position: absolute; left: 0; right: 0; top: 560px; height: 46px;
    background: var(--grey);
    display: flex; align-items: center; justify-content: center;
    color: var(--white); font-weight: 600; font-size: 19px;
  }

  .back-pattern {
    position: absolute; inset: 0;
    background: linear-gradient(160deg, #3a3a3c 0%, #242425 45%, #151515 100%);
  }
  .back-mark {
    position: absolute; left: 232px; top: 448px;
    font-weight: 800; font-size: 28px; line-height: 1;
    color: var(--orange);
  }
</style>
</head>
<body>
<main class="stage">
  <section class="card card--front" aria-label="Card front">
    <div class="brand-mark">KT Crewing</div>
    <div class="contact">
      <p class="contact__name">MICK HARLOW</p>
      <p class="contact__role">Managing Director</p>
      <div class="contact__rule"></div>
      <p class="contact__line">0431 256 049</p>
      <p class="contact__line">Mick@ktcrewing.com.au</p>
      <div class="contact__rule"></div>
      <p class="contact__line"><span class="contact__label">ACN:</span> 718 235 946</p>
    </div>
    <div class="slogan-band">Onsite Auto Electrician Labour hire</div>
  </section>

  <section class="card card--back" aria-label="Card back">
    <div class="back-pattern" role="img" aria-label="Repeating tonal brand pattern in dark greys"></div>
    <div class="back-mark">KT Crewing</div>
  </section>
</main>
</body>
</html>
```